Real Estate Window Sign

This will be a real estate window sign for the following office, pictures attached for the office and pictures included as to what needs to be on the signs.
windows on the right side of the office are 2 storeys in height. This can be several window coverings or one huge one that will be divided up to form a few different smaller ones. There is also a window beside the door to be used with a phone number, name etc whatever you feel relevant. The upper windows are too high to see as walker bys so maybe graphics should go up there?

Target Market(s)

Walk by traffic for real estate

Industry/Entity Type

Real Estate

Colors
fbee3d

Requirements
Must have
• My company logo (in pics)
• My name etc as appearing on Card
• My company name as appearing on card
• Writeup:
• HARBOUR POINT
• -SALES
• -RENTALS
• -PROPERTY MANAGEMENT
Nice to have
• cool colour designs (see logos etc)

```html
<!DOCTYPE html>
<html lang="en">
<head>
<meta charset="utf-8">
<title>Daniel Ashford – Real Estate Window Sign</title>
<link rel="stylesheet" href="https://fonts.googleapis.com/css2?family=Cinzel:wght@400;600&display=swap">
<style>
  :root {
    --page-bg: #ffffff;
    --sign-edge: #c9c9c9;
    --sign-light: #ffffff;
    --ink: #111111;
    --ink-soft: #555555;
    --brand-blue: #2b4f9e;
    --band: #000000;
    --band-text: #ffffff;
    --circle-text: #ffffff;
  }
  * { margin: 0; padding: 0; box-sizing: border-box; }
  html, body {
    width: 1200px; height: 706px; overflow: hidden;
    background: var(--page-bg);
  }
  .canvas { position: relative; width: 1200px; height: 706px; }
  .window-sign {
    position: absolute; left: 495px; top: 23px;
    width: 210px; height: 660px;
    background: linear-gradient(to bottom, var(--sign-edge) 0%, #efefef 22%, var(--sign-light) 45%, #f2f2f2 70%, var(--sign-edge) 100%);
    font-family: "Cinzel", "Times New Roman", serif;
    box-shadow: 0 0 6px rgba(0,0,0,0.25);
  }
  .brand-mark {
    position: absolute; top: 100px; left: 88px;
    width: 34px; height: 34px;
    background: var(--brand-blue);
  }
  .brand {
    position: absolute; top: 193px; left: 0; width: 100%;
    text-align: center;
  }
  .brand-name {
    font-size: 16px; font-weight: 600; color: var(--ink);
    letter-spacing: 0.3px; white-space: nowrap; line-height: 18px;
  }
  .brand-title {
    font-size: 9px; color: var(--ink-soft);
    letter-spacing: 0.6px; line-height: 11px;
  }
  .services {
    position: absolute; top: 272px; left: 0; width: 210px; height: 210px;
  }
  .services text {
    font-family: "Cinzel", "Times New Roman", serif;
    fill: var(--circle-text); text-anchor: middle; font-weight: 400;
  }
  .contact-band {
    position: absolute; left: 0; top: 523px; width: 100%; height: 86px;
    background: var(--band); color: var(--band-text);
    display: flex; flex-direction: column; justify-content: center;
    align-items: center; font-size: 9.5px; line-height: 14.5px;
    font-variant: small-caps;
  }
  .contact-band .web { font-size: 8.5px; }
</style>
</head>
<body>
<main class="canvas">
  <section class="window-sign">
    <span class="brand-mark" aria-hidden="true"></span>
    <header class="brand">
      <h1 class="brand-name">Daniel Ashford</h1>
      <p class="brand-title">Real Estate Broker</p>
    </header>

    <svg class="services" viewBox="0 0 210 210" aria-label="Harbour Point: sales, rentals, property management">
      <defs>
        <radialGradient id="blueFill" cx="40%" cy="35%" r="70%">
          <stop offset="0%" stop-color="#3d66bd"/>
          <stop offset="100%" stop-color="#1a3574"/>
        </radialGradient>
        <radialGradient id="blackFill" cx="40%" cy="35%" r="70%">
          <stop offset="0%" stop-color="#333333"/>
          <stop offset="100%" stop-color="#000000"/>
        </radialGradient>
        <radialGradient id="greyFill" cx="40%" cy="35%" r="70%">
          <stop offset="0%" stop-color="#8a8a8a"/>
          <stop offset="100%" stop-color="#444444"/>
        </radialGradient>
      </defs>
      <circle class="service area" cx="68" cy="53" r="44" fill="url(#blueFill)" stroke="#fff" stroke-width="1.5"/>
      <text x="68" y="49" font-size="12.5">HARBOUR</text>
      <text x="68" y="63" font-size="12.5">POINT</text>

      <circle class="service rentals" cx="75" cy="121" r="37" fill="url(#greyFill)" stroke="#fff" stroke-width="1.5"/>
      <text x="72" y="125" font-size="12">RENTALS</text>

      <circle class="service sales" cx="128" cy="86" r="33" fill="url(#blackFill)" stroke="#fff" stroke-width="1.5"/>
      <text x="128" y="90" font-size="12.5">SALES</text>

      <circle class="service property" cx="137" cy="157" r="48" fill="url(#blueFill)" stroke="#fff" stroke-width="1.5"/>
      <text x="137" y="154" font-size="12.5">PROPERTY</text>
      <text x="137" y="166" font-size="9">MANAGEMENT</text>
    </svg>

    <footer class="contact-band">
      <span>Office: (555) 214-3380</span>
      <span>Cell: (555) 672-9014</span>
      <span>Fax: (555) 214-3391</span>
      <span class="web">www.harbourlinehomes.com</span>
    </footer>
  </section>
</main>
</body>
</html>
```